Create a sign for my school of biodynamic craniosacral therapy: Lumen Harbor

Hello, I would like to get a designer to make me a sign. I have a logo in mind. The sign will be about 7' X 3' or 4' big. ( in feet)
I have another site to transfer the design to make the sign with.
I attached a few logos I like. I need the sign to be easy to read for cars driving by, without too much information. I would like it to look original and holistic. Also have a whimsical and sky and earth quality.
my website will give you a feel www.lumenharbor.example
The last picture of the "Tarn Goods" sign is a sample of how I will make the entire sign structure.

Target Market(s)

body worker students

Industry/Entity Type

School and healthcare

Font styles to use
Decorative
Other font styles liked:
• dead hardy, milonga, ribeye,sketch block , train one

Colors

Designer to choose colors to be used in the design.

Requirements
Must have
• easy to read, highly visible, organic looking
Nice to have
• simular to my design
Should not have
• look too commercial

```html
<!DOCTYPE html>
<html lang="en">
<head>
<meta charset="utf-8">
<title>Lumen Harbor – School and Practice Sign</title>
<link rel="stylesheet" href="https://fonts.googleapis.com/css2?family=Alfa+Slab+One&family=Milonga&family=Archivo+Black&display=swap">
<style>
  :root {
    --frame: #314519;
    --bg-light: #e4e5e4;
    --bg-dark: #a9aaa9;
    --plaque-lime: #a0c41c;
    --plaque-light: #9de35a;
    --plaque-mid: #6ec030;
    --ink: #314519;
    --white: #ffffff;
    --sky-top: #0a1930;
    --sky-mid: #0d2f5c;
    --horizon: #061020;
    --hill-dark: #4f8f26;
    --hill-light: #a3c61a;
  }
  * { box-sizing: border-box; margin: 0; padding: 0; }
  html, body { width: 1200px; height: 1200px; overflow: hidden; }
  body {
    position: relative;
    background: radial-gradient(ellipse at 50% 45%, var(--bg-light) 0%, #cfd0cf 55%, var(--bg-dark) 100%);
  }
  .sign { position: absolute; inset: 0; }
  .post {
    position: absolute;
    top: 165px;
    width: 35px;
    height: 850px;
    background: var(--frame);
  }
  .post--left { left: 177px; }
  .post--right { left: 987px; }
  .rail {
    position: absolute;
    height: 17px;
    width: 22px;
    border-top: 5px solid var(--frame);
    border-bottom: 5px solid var(--frame);
  }
  .rail--left { left: 209px; }
  .rail--right { left: 967px; }

  .header-panel {
    position: absolute;
    left: 211px;
    top: 163px;
    width: 776px;
    height: 377px;
    border: 7px solid var(--frame);
    border-radius: 124px;
    overflow: hidden;
  }
  .header-scene {
    position: absolute;
    inset: 0;
    background: linear-gradient(180deg,
      var(--sky-top) 0%,
      var(--sky-mid) 40%,
      var(--horizon) 62%,
      var(--hill-dark) 70%,
      var(--hill-light) 100%);
  }
  .school-name {
    position: absolute;
    left: 0; right: 0;
    top: 74px;
    text-align: center;
    font-family: "Alfa Slab One", serif;
    font-size: 66px;
    font-weight: 400;
    letter-spacing: 1px;
    color: var(--white);
    line-height: 1;
    white-space: nowrap;
  }
  .school-tagline {
    position: absolute;
    left: 0; right: 0;
    top: 142px;
    text-align: center;
    font-family: "Milonga", serif;
    font-size: 51px;
    color: var(--white);
    line-height: 1;
    white-space: nowrap;
  }

  .plaque {
    position: absolute;
    left: 229px;
    width: 738px;
    height: 121px;
    border: 8px solid var(--frame);
    color: var(--ink);
    text-align: center;
    display: flex;
    flex-direction: column;
    justify-content: center;
    gap: 2px;
  }
  .plaque--training { top: 568px; height: 122px; background: var(--plaque-lime); }
  .plaque--chiro { top: 705px; background: var(--plaque-light); }
  .plaque--cranial { top: 837px; background: var(--plaque-mid); }
  .plaque__script {
    font-family: "Milonga", serif;
    font-size: 32px;
    line-height: 1.1;
    white-space: nowrap;
  }
  .plaque__bold {
    font-family: "Archivo Black", sans-serif;
    font-size: 37px;
    letter-spacing: 1px;
    word-spacing: 6px;
    line-height: 1.1;
    white-space: nowrap;
  }
  .plaque__bold--long {
    font-size: 31px;
    letter-spacing: 0;
    word-spacing: 5px;
  }
</style>
</head>
<body>
  <main class="sign">
    <div class="post post--left"></div>
    <div class="post post--right"></div>

    <div class="rail rail--left" style="top:621px"></div>
    <div class="rail rail--right" style="top:621px"></div>
    <div class="rail rail--left" style="top:757px"></div>
    <div class="rail rail--right" style="top:757px"></div>
    <div class="rail rail--left" style="top:889px"></div>
    <div class="rail rail--right" style="top:889px"></div>

    <section class="header-panel">
      <div class="header-scene" role="img" aria-label="Night sky with stars and constellations above rolling green hills and pine trees, with a faceted purple and teal bear walking across the meadow"></div>
      <h1 class="school-name">LUMEN HARBOR</h1>
      <p class="school-tagline">School and Practice</p>
    </section>

    <section class="plaque plaque--training">
      <p class="plaque__script">lumenharbor.example</p>
      <p class="plaque__bold plaque__bold--long">Biodynamic Craniosacral Trainings</p>
    </section>

    <section class="plaque plaque--chiro">
      <p class="plaque__bold">Dr Mara Vossen</p>
      <p class="plaque__script">Chiropractic. Cranial. Nutrition</p>
    </section>

    <section class="plaque plaque--cranial">
      <p class="plaque__bold">Elsa Vossen, BA, RT, BCST</p>
      <p class="plaque__script">Cranial Therapist</p>
    </section>
  </main>
</body>
</html>
```